Halvern Drywork Business Card Design

Professional and clean design. The design colors should flow with the logo. Two-sided card with the website on the back which is:

www.HalvernDrywork.example.

"Specializing in Water Damage Restoration"

On the front I need the name, email, phone, and logo.

Name: Dorian Kettleby
Email: Dorian@HalvernDrywork.example
Phone: 555-0142-836 for now

I only have the Preview and Thumbnail right now but should have the source files uploaded within a day or two.

Target Market(s)

Flood victims, home owners with water damage from busted pipes etc...

Industry/Entity Type

Business

Contact Information for Business Card

Name: Dorian Kettleby

Font styles to use
Serif
Sans Serif

```html
<!DOCTYPE html>
<html lang="en">
<head>
<meta charset="UTF-8">
<title>Halvern Drywork Business Card</title>
<link rel="stylesheet" href="https://fonts.googleapis.com/css2?family=Cinzel:wght@500;600&family=Source+Sans+3:wght@400;600&display=swap">
<style>
  :root {
    --page-bg: #e9ecef;
    --blue-light: #5bb8ec;
    --blue-mid: #2f9ad8;
    --blue-deep: #1a7fc1;
    --card-white: #ffffff;
    --card-shade: #eef1f4;
    --text-grey: #4a4f55;
    --icon-blue: #3a9ad9;
  }
  * { margin: 0; padding: 0; box-sizing: border-box; }
  html, body { width: 1200px; height: 843px; overflow: hidden; }
  body {
    background: var(--page-bg);
    font-family: "Source Sans 3", Arial, sans-serif;
    position: relative;
  }
  .card {
    position: absolute;
    left: 290px;
    width: 620px;
    height: 354px;
    border-radius: 22px;
    overflow: hidden;
    box-shadow: 0 10px 28px rgba(0,0,0,0.18);
  }
  /* Back side */
  .card-back {
    top: 52px;
    background: linear-gradient(135deg, var(--blue-light) 0%, var(--blue-mid) 55%, var(--blue-deep) 100%);
    color: var(--card-white);
    text-align: center;
  }
  .back-mark {
    position: absolute;
    top: 62px;
    left: 50%;
    transform: translateX(-50%);
    display: flex;
    flex-direction: column;
    align-items: center;
    gap: 14px;
  }
  .mark-circle {
    width: 96px;
    height: 96px;
    border-radius: 50%;
    background: var(--card-white);
  }
  .back-name {
    font-family: "Cinzel", Georgia, serif;
    font-weight: 600;
    font-size: 30px;
    letter-spacing: 2px;
    color: var(--card-white);
    white-space: nowrap;
  }
  .back-tagline {
    position: absolute;
    bottom: 70px;
    width: 100%;
    font-weight: 600;
    font-size: 19px;
    letter-spacing: 0.3px;
  }
  .back-web {
    position: absolute;
    bottom: 38px;
    width: 100%;
    font-size: 17px;
    opacity: 0.92;
  }
  /* Front side */
  .card-front {
    top: 438px;
    background: linear-gradient(160deg, var(--card-white) 55%, var(--card-shade) 100%);
  }
  .name-band {
    position: absolute;
    top: 64px;
    left: 0;
    width: 440px;
    height: 46px;
    background: linear-gradient(90deg, var(--blue-light), var(--blue-deep));
    display: flex;
    align-items: center;
    padding-left: 34px;
  }
  .person-name {
    font-family: "Cinzel", Georgia, serif;
    font-weight: 500;
    font-size: 25px;
    letter-spacing: 1px;
    color: var(--card-white);
  }
  .front-mark {
    position: absolute;
    top: 58px;
    right: 34px;
    display: flex;
    flex-direction: column;
    align-items: center;
    gap: 10px;
  }
  .front-mark .mark-circle {
    width: 60px;
    height: 60px;
    background: var(--blue-mid);
    border: 3px solid var(--card-white);
  }
  .front-name {
    font-family: "Cinzel", Georgia, serif;
    font-weight: 600;
    font-size: 27px;
    letter-spacing: 1px;
    color: var(--blue-mid);
    white-space: nowrap;
  }
  .contact-list {
    position: absolute;
    left: 40px;
    bottom: 40px;
    list-style: none;
    font-size: 16px;
    color: var(--text-grey);
  }
  .contact-list li {
    display: flex;
    align-items: center;
    gap: 8px;
    margin-top: 7px;
  }
  .contact-row { display: flex; gap: 28px; }
  .contact-list svg { width: 15px; height: 15px; fill: var(--icon-blue); flex-shrink: 0; }
</style>
</head>
<body>
  <section class="card card-back">
    <div class="back-mark">
      <div class="mark-circle"></div>
      <div class="back-name">Halvern Drywork</div>
    </div>
    <p class="back-tagline">Specializing in Water Damage Restoration</p>
    <p class="back-web">www.HalvernDrywork.example</p>
  </section>

  <section class="card card-front">
    <div class="name-band"><span class="person-name">Dorian Kettleby</span></div>
    <div class="front-mark">
      <div class="mark-circle"></div>
      <div class="front-name">Halvern Drywork</div>
    </div>
    <ul class="contact-list">
      <li class="contact-row">
        <span style="display:flex;align-items:center;gap:8px">
          <svg viewBox="0 0 24 24" aria-hidden="true"><path d="M6.6 10.8a15.1 15.1 0 0 0 6.6 6.6l2.2-2.2a1 1 0 0 1 1-.25 11.4 11.4 0 0 0 3.6.57 1 1 0 0 1 1 1V20a1 1 0 0 1-1 1A17 17 0 0 1 3 4a1 1 0 0 1 1-1h3.5a1 1 0 0 1 1 1c0 1.25.2 2.45.57 3.57a1 1 0 0 1-.25 1z"/></svg>
          555-0142-836 for now
        </span>
      </li>
      <li>
        <svg viewBox="0 0 24 24" aria-hidden="true"><path d="M3 5h18a1 1 0 0 1 1 1v12a1 1 0 0 1-1 1H3a1 1 0 0 1-1-1V6a1 1 0 0 1 1-1zm9 7.2L20 7H4z"/></svg>
        Dorian@HalvernDrywork.example
      </li>
      <li>
        <svg viewBox="0 0 24 24" aria-hidden="true"><path d="M12 2a10 10 0 1 0 0 20 10 10 0 0 0 0-20zm6.9 6h-2.9a15.6 15.6 0 0 0-1.4-3.6A8 8 0 0 1 18.9 8zM12 4c.8 1.2 1.5 2.5 1.9 4h-3.8c.4-1.5 1.1-2.8 1.9-4zM4.3 14a8 8 0 0 1 0-4h3.4a16.5 16.5 0 0 0 0 4zm.8 2h2.9c.3 1.3.8 2.5 1.4 3.6A8 8 0 0 1 5.1 16zM8 8H5.1a8 8 0 0 1 4.3-3.6C8.8 5.5 8.3 6.7 8 8zm4 12c-.8-1.2-1.5-2.5-1.9-4h3.8c-.4 1.5-1.1 2.8-1.9 4zm2.3-6H9.7a14.7 14.7 0 0 1 0-4h4.6a14.7 14.7 0 0 1 0 4zm.3 5.6c.6-1.1 1.1-2.3 1.4-3.6h2.9a8 8 0 0 1-4.3 3.6zm1.7-5.6a16.5 16.5 0 0 0 0-4h3.4a8 8 0 0 1 0 4z"/></svg>
        www.HalvernDrywork.example
      </li>
    </ul>
  </section>
</body>
</html>
```